Package design for a high-visibility children's commuter safety kit

As per the attached files (2+3) the kit contains a high-visibility vest, reflective snap bands as well as a novelty sticker and key ring. We have a particular layout in mind and the packaging design needs to accommodate these layout requirements. The package is 43cm in height and 26cm in width with a gap of 4cm across the top between the plastic covering the products and edge of the cardboard end and 5cm between the plastic covering and the right hand side of the cardboard. These gaps are the work area for the proposed designs on a black cardboard backing. In the design area we require the attached Brimvale logo
(File 1) and the description of the product (i.e. 'Child Commuter Safety Kit'). We are also considering having the contents listed for each item (e.g. Reflective vest/3 x reflective snap bands/Smiley sticker/Key ring). The design must keep in mind that the kits will be for children aged 5-15 years of age and primarily marketed towards children as well as concerned adults.

Plastic

```html
<!DOCTYPE html>
<html lang="en">
<head>
<meta charset="utf-8">
<title>Brimvale Child Commuter Safety Kit – Package Front</title>
<link rel="stylesheet" href="https://fonts.googleapis.com/css2?family=Arimo:ital,wght@0,400;0,700;1,700&display=swap">
<style>
  :root {
    --page: #ffffff;
    --card: #000000;
    --lime: #b8d43a;
    --lime-light: #cddd3c;
    --lime-deep: #a9cb3a;
    --text-light: #d4d4d4;
    --band-white: #ececec;
    --ink: #111111;
    --sign-red: #d9262c;
    --sign-orange: #f2a23a;
    --sign-blue: #3aa7d8;
    --bubble-tone: #dfe9b8;
  }
  * { margin: 0; padding: 0; box-sizing: border-box; }
  html, body {
    width: 900px; height: 1200px; overflow: hidden;
    background: var(--page);
    font-family: "Arimo", Arial, sans-serif;
  }
  .package {
    position: absolute; left: 147px; top: 65px;
    width: 634px; height: 1048px;
    background: var(--card);
    overflow: hidden;
  }
  .brand {
    position: absolute; left: 38px; top: 20px;
    display: flex; align-items: center; gap: 10px;
  }
  .brand__square {
    width: 54px; height: 54px; background: var(--lime);
  }
  .brand__name {
    font-size: 50px; font-weight: 400; color: var(--text-light);
    letter-spacing: -0.5px; line-height: 1;
  }
  .product-title {
    position: absolute; left: 306px; top: 34px;
    color: var(--text-light); font-size: 16px; font-weight: 700; line-height: 18px;
  }
  .bubbles {
    position: absolute;
    background: radial-gradient(ellipse at 70% 50%, rgba(223,233,184,0.28), rgba(223,233,184,0.06) 60%, rgba(0,0,0,0) 80%);
  }
  .bubbles--top { left: 443px; top: 5px; width: 191px; height: 235px; }
  .bubbles--mid { left: 518px; top: 385px; width: 116px; height: 105px; }
  .overlay { position: absolute; left: 0; top: 0; }
  .age-band {
    position: absolute; left: 0; bottom: 0; width: 634px; height: 98px;
    background: linear-gradient(90deg, var(--lime-deep), var(--lime-light));
  }
  .age-band__text {
    position: absolute; right: 15px; top: 39px;
    font-size: 18px; font-weight: 700; color: var(--ink);
  }
  .content-label { font-family: "Arimo", Arial, sans-serif; font-weight: 700; font-size: 14px; fill: var(--ink); }
  .content-label--italic { font-style: italic; }
</style>
</head>
<body>
<div class="package">
  <div class="brand">
    <div class="brand__square"></div>
    <div class="brand__name">Brimvale</div>
  </div>
  <div class="product-title">Child Commuter<br>Safety Kit</div>

  <div class="bubbles bubbles--top" role="img" aria-label="Scattered glowing bubble decoration"></div>
  <div class="bubbles bubbles--mid" role="img" aria-label="Scattered glowing bubble decoration"></div>

  <svg class="overlay" width="634" height="1048" viewBox="0 0 634 1048" xmlns="http://www.w3.org/2000/svg">
    <!-- product window frame -->
    <polyline points="0,103 481,103 510,132 510,950" fill="none" stroke="var(--lime)" stroke-width="3"/>

    <!-- contents list -->
    <g class="contents-list">
      <polygon points="510,260 634,244 634,266 510,283" fill="var(--lime)"/>
      <text class="content-label content-label--italic" transform="translate(522,276) rotate(-7)">Reflective vest</text>

      <polygon points="510,285 634,268 634,312 510,330" fill="var(--band-white)"/>
      <text class="content-label" transform="translate(536,301) rotate(-7)">Reflective</text>
      <text class="content-label" transform="translate(532,318) rotate(-7)">Snap Bands</text>

      <polygon points="510,333 634,316 634,340 510,358" fill="var(--lime)"/>
      <text class="content-label content-label--italic" transform="translate(522,351) rotate(-7)">Smiley sticker</text>

      <polygon points="510,362 634,345 634,382 510,400" fill="var(--band-white)"/>
      <text class="content-label" transform="translate(546,389) rotate(-7)">Key ring</text>
    </g>

    <!-- road safety signs -->
    <g class="warning-sign">
      <polygon points="572,520 610,583 534,583" fill="var(--sign-red)"/>
      <polygon points="572,536 597,577 547,577" fill="#ffffff"/>
      <rect x="569" y="547" width="6" height="18" rx="2" fill="var(--ink)"/>
      <circle cx="572" cy="571" r="3.5" fill="var(--ink)"/>
    </g>
    <polygon class="school-sign" role="img" aria-label="Children crossing warning sign" points="575,612 613,677 537,677" fill="var(--sign-orange)" stroke="var(--sign-red)" stroke-width="5" stroke-linejoin="round"/>
    <rect class="pedestrian-sign" role="img" aria-label="Pedestrian zone sign" x="537" y="710" width="72" height="72" rx="6" fill="var(--sign-blue)" stroke="#ffffff" stroke-width="3"/>
    <rect class="play-street-sign" role="img" aria-label="Child on tricycle sign" x="537" y="818" width="72" height="72" rx="6" fill="var(--sign-blue)" stroke="#ffffff" stroke-width="3"/>
  </svg>

  <div class="age-band">
    <div class="age-band__text">5-15 years</div>
  </div>
</div>
</body>
</html>
```